"Vows and Farewells by Meg" Web Site

I would like a web site designed for my funeral and wedding celebrancy business. My logo was designed by Artboard Hive (attached). I have written content of the web pages for reference (attached). I have attached logos designed through artboard hive and photos.
I am sure what else to write in a project description and would welcome suggestions

Target Market(s)

for marriages - brides and grooms, for funerals - families who have lost a loved one

Industry/Entity Type

Wedding Planner

Number of Pages Required

4 page

Font styles to use
Sans Serif

Colors
886aae
3277b5
33a6d7
a64599
e34096

Requirements
Must have
• a call to action (contact me) throughout
Nice to have
• nil
Should not have
• no morbid images

```html
<!DOCTYPE html>
<html lang="en">
<head>
<meta charset="utf-8">
<title>Vows and Farewells by Meg</title>
<link href="https://fonts.googleapis.com/css2?family=Open+Sans:wght@400;600&family=Roboto+Condensed:wght@400;700&family=Oswald:wght@500&display=swap" rel="stylesheet">
<style>
:root{
  --purple:#8e2f8c;
  --purple-soft:#a64599;
  --pink:#d4147f;
  --pink-bright:#e34096;
  --blue:#3277b5;
  --blue-light:#4a8fcf;
  --grey-bg:#ebebeb;
  --ink:#222222;
  --text:#444444;
  --footer:#0d0d0d;
  --footer-bar:#050505;
  --white:#ffffff;
}
*{margin:0;padding:0;box-sizing:border-box}
html,body{width:1200px;height:2616px;overflow:hidden}
body{position:relative;background:var(--grey-bg);font-family:"Open Sans",Arial,sans-serif;color:var(--text)}
.abs{position:absolute}

/* header */
.site-header{position:absolute;left:0;top:0;width:1200px;height:129px}
.phone-badge{left:89px;top:42px;width:48px;height:48px;border:2px solid #d9d9d9;border-radius:50%;background:var(--white);display:flex;align-items:center;justify-content:center}
.phone-label{left:153px;top:38px;font-size:17px;line-height:22px;color:var(--ink)}
.phone-number{left:153px;top:68px;font-size:14px;line-height:18px;color:var(--ink)}
.brand{left:440px;top:42px;width:320px;text-align:center}
.brand-mark{display:block;width:40px;height:40px;border-radius:50%;background:#8e6aa8;margin:0 auto 6px}
.brand-name{display:block;font-family:"Roboto Condensed",Arial,sans-serif;font-size:20px;line-height:24px;color:#6b4e8a;letter-spacing:.5px;white-space:nowrap}
.cta-button{left:982px;top:38px;width:127px;height:42px;border-radius:21px;background:var(--purple);color:var(--white);font-size:15px;display:flex;align-items:center;justify-content:center}

/* nav */
.main-nav{left:89px;top:129px;width:1022px;height:59px;background:linear-gradient(180deg,var(--blue-light),var(--blue));display:flex}
.main-nav a{color:var(--white);text-decoration:none;font-size:17px;display:flex;align-items:center;justify-content:center}
.main-nav .active{background:var(--purple);width:146px}

/* hero */
.hero{left:89px;top:188px;width:1022px;height:506px;background:linear-gradient(120deg,#6d5a4a 0%,#b9a48e 35%,#e8e0d6 55%,#9c8a78 80%,#5b4c40 100%)}
.hero-title{left:142px;top:550px;font-family:"Oswald",Arial,sans-serif;font-weight:500;font-size:46px;line-height:54px;color:var(--white);letter-spacing:.5px;white-space:nowrap}
.hero-sub{left:142px;top:609px;font-size:20px;line-height:26px;color:var(--white);white-space:nowrap}
.slider-arrows{left:1040px;top:650px;display:flex;gap:10px}

/* services band */
.services{left:0;top:694px;width:1200px;height:572px;background:radial-gradient(circle at 30% 40%,#e0348f 0%,var(--pink) 55%,#c10f73 100%)}
.service-tile{top:698px;height:239px;border:1px solid rgba(255,255,255,.7)}
.service-tile span{position:absolute;left:0;right:0;bottom:20px;text-align:center;font-family:"Roboto Condensed",Arial,sans-serif;font-size:30px;line-height:36px;color:var(--white)}
.tile-marriages{left:89px;width:340px;background:linear-gradient(160deg,#5e7a45,#c7c0b5 60%,#8a7f78)}
.tile-funerals{left:431px;width:340px;background:linear-gradient(160deg,#3a302b,#8c7565 55%,#2b2522)}
.tile-ceremonies{left:773px;width:338px;background:linear-gradient(180deg,#9cb8cf,#c9c4b8 60%,#8a7b6a)}
.welcome-title{left:0;width:1200px;top:998px;text-align:center;font-family:"Roboto Condensed",Arial,sans-serif;font-weight:400;font-size:34px;line-height:40px;color:var(--white)}
.welcome-text{left:252px;width:696px;top:1052px;text-align:center;font-size:16px;line-height:26px;color:var(--white)}
.read-more-blue{left:534px;top:1155px;width:132px;height:41px;border-radius:21px;background:var(--blue);color:var(--white);font-size:15px;display:flex;align-items:center;justify-content:center}

/* about */
.about-card{left:148px;top:1353px;width:898px;height:328px;background:var(--white);box-shadow:0 8px 24px rgba(0,0,0,.18)}
.about-body{left:187px;top:1398px;width:420px;display:flex;flex-direction:column;align-items:flex-start}
.about-title{font-family:"Roboto Condensed",Arial,sans-serif;font-weight:400;font-size:34px;line-height:42px;color:var(--ink)}
.about-text{margin-top:8px;font-size:15px;line-height:25px;color:var(--text);text-align:justify}
.read-more-purple{margin-top:16px;width:109px;height:33px;border-radius:17px;background:var(--purple);color:var(--white);font-size:12px;display:flex;align-items:center;justify-content:center}
.about-video{left:654px;top:1353px;width:392px;height:328px;background:linear-gradient(135deg,#d8d8de,#a49aa0 50%,#4b6a60)}
.play-button{left:816px;top:1484px;width:64px;height:64px;border-radius:50%;background:rgba(0,0,0,.55);display:flex;align-items:center;justify-content:center}

/* blog */
.blog{left:0;top:1750px;width:1200px;height:531px;background:var(--white)}
.blog-title{left:0;width:1200px;top:1844px;text-align:center;font-family:"Roboto Condensed",Arial,sans-serif;font-weight:400;font-size:34px;line-height:40px;color:var(--ink)}
.post{top:1924px;width:312px}
.post-image{height:172px;position:relative}
.post-meta{position:absolute;left:0;bottom:0;display:flex;height:22px;font-size:12px;color:var(--white)}
.post-date{background:var(--blue);width:70px;display:flex;align-items:center;justify-content:center}
.post-comments{background:var(--pink-bright);width:34px;display:flex;align-items:center;justify-content:center;gap:3px}
.post h3{font-weight:400;font-size:17px;line-height:22px;color:var(--ink);margin-top:22px}
.post p{font-size:13px;line-height:20px;color:#555;margin-top:8px}
.post a{display:block;font-size:13px;color:var(--pink-bright);text-decoration:none;margin-top:6px}
.post-1{left:89px}.post-1 .post-image{background:linear-gradient(135deg,#7a5a45,#c08a6a 50%,#3a2a25)}
.post-2{left:436px}.post-2 .post-image{background:linear-gradient(180deg,#1f3a66,#6c7aa0 50%,#c9b8a4)}
.post-3{left:792px}.post-3 .post-image{background:linear-gradient(135deg,#9a4a30,#e2b79c 50%,#f2e5da)}

/* footer */
.site-footer{left:0;top:2281px;width:1200px;height:262px;background:var(--footer);color:var(--white)}
.footer-brand{left:58px;top:2385px;width:240px;text-align:center}
.footer-brand .brand-mark{background:var(--white);width:34px;height:34px}
.footer-brand .brand-name{color:var(--white);font-size:17px;line-height:22px}
.footer-heading{top:2357px;font-size:15px;line-height:20px;letter-spacing:.3px;color:var(--white)}
.contact-list{left:366px;top:2394px;list-style:none;font-size:13px;line-height:20px;color:var(--white)}
.contact-list li{display:flex;gap:12px;margin-bottom:8px}
.contact-list svg{flex:none;margin-top:3px}
.newsletter-note{left:647px;top:2392px;width:210px;font-size:12px;line-height:18px;color:var(--white)}
.newsletter-form{left:647px;top:2435px;display:flex;color:var(--white)}
.newsletter-form .field{width:148px;height:30px;background:var(--white);color:#777;font-size:12px;line-height:16px;padding:7px 8px}
.newsletter-form .submit{width:55px;height:30px;background:var(--pink-bright);font-size:12px;display:flex;align-items:center;justify-content:center}
.social{left:942px;top:2396px;display:flex;gap:13px}
.social span{width:26px;height:26px;border-radius:4px;background:var(--white)}
.footer-bar{left:0;top:2543px;width:1200px;height:73px;background:var(--footer-bar);color:var(--white);font-size:13px;display:flex;align-items:center;justify-content:center}
</style>
</head>
<body>

<header class="site-header">
  <div class="abs phone-badge">
    <svg width="22" height="22" viewBox="0 0 24 24"><path fill="#d4147f" d="M6.6 10.8c1.4 2.8 3.8 5.1 6.6 6.6l2.2-2.2c.3-.3.7-.4 1-.2 1.1.4 2.3.6 3.6.6.6 0 1 .4 1 1V20c0 .6-.4 1-1 1C10.6 21 3 13.4 3 4c0-.6.4-1 1-1h3.5c.6 0 1 .4 1 1 0 1.3.2 2.5.6 3.6.1.3 0 .7-.2 1z"/></svg>
  </div>
  <div class="abs phone-label">Phone</div>
  <div class="abs phone-number">+32 (0)2 555 0148</div>
  <div class="abs brand"><span class="brand-mark"></span><span class="brand-name">Vows and Farewells by Meg</span></div>
  <div class="abs cta-button">Contact Me</div>
</header>

<nav class="abs main-nav">
  <a class="active" href="#">Home</a>
  <a href="#" style="width:132px">About us</a>
  <a href="#" style="width:150px">Marriages</a>
  <a href="#" style="width:140px">Funerals</a>
  <a href="#" style="width:240px">Other Ceremonies</a>
  <a href="#" style="width:214px">Contact Me</a>
</nav>

<div class="abs hero" role="img" aria-label="Photo of a smiling bride and groom celebrating outdoors"></div>
<div class="abs hero-title">VOWS AND FAREWELLS BY MEG</div>
<div class="abs hero-sub">Funeral and wedding celebration business</div>
<div class="abs slider-arrows">
  <svg width="16" height="16" viewBox="0 0 16 16"><path d="M10 3 5 8l5 5" fill="none" stroke="#fff" stroke-width="2"/></svg>
  <svg width="16" height="16" viewBox="0 0 16 16"><path d="M6 3l5 5-5 5" fill="none" stroke="#fff" stroke-width="2"/></svg>
</div>

<section class="abs services" aria-label="Services"></section>
<div class="abs service-tile tile-marriages" role="img" aria-label="Photo of a bride with the celebrant in a garden"><span>Marriages</span></div>
<div class="abs service-tile tile-funerals" role="img" aria-label="Photo of white lilies at a memorial service"><span>Funerals</span></div>
<div class="abs service-tile tile-ceremonies" role="img" aria-label="Photo of the celebrant on a beach with a couple"><span>Other Ceremonies</span></div>
<h2 class="abs welcome-title">Welcome to Vows and Farewells by Meg</h2>
<p class="abs welcome-text">Thank you for visiting ‘Vows and Farewells by Meg’. Whether you are planning a wedding with the love of your life, a funeral to celebrate the life of a loved one or one of many other love and life celebrations, I am glad that you came to ‘Vows and Farewells by Meg’.</p>
<div class="abs read-more-blue">Read More</div>

<div class="abs about-card"></div>
<div class="abs about-body">
  <h2 class="about-title">About me</h2>
  <p class="about-text">My name is Meg Hartwell and I am the owner of ‘Vows and Farewells by Meg’. I trained as a civil celebrant as I wanted to add this important and meaningful work to my diverse portfolio career. I am also the business owner of Larchmont Leadership and Consulting where I consult to organisations</p>
  <div class="read-more-purple">READ MORE</div>
</div>
<div class="abs about-video" role="img" aria-label="Video still of the celebrant speaking into a microphone"></div>
<div class="abs play-button"><svg width="26" height="26" viewBox="0 0 24 24"><path d="M7 4v16l13-8z" fill="#fff"/></svg></div>

<section class="abs blog"></section>
<h2 class="abs blog-title">Latest Blog</h2>
<article class="abs post post-1">
  <div class="post-image" role="img" aria-label="Photo of red roses resting on a wooden casket">
    <div class="post-meta"><span class="post-date">Dec 03</span><span class="post-comments"><svg width="12" height="10" viewBox="0 0 12 10"><path d="M1 1h10v6H5L2 9V7H1z" fill="none" stroke="#fff"/></svg>0</span></div>
  </div>
  <h3>Neque porro quisquam dolorem</h3>
  <p>It has survived not only five centuries, but also the leap into electronic typesetting,</p>
  <a href="#">Read More »</a>
</article>
<article class="abs post post-2">
  <div class="post-image" role="img" aria-label="Photo of a reception table under string lights">
    <div class="post-meta"><span class="post-date">Dec 03</span><span class="post-comments"><svg width="12" height="10" viewBox="0 0 12 10"><path d="M1 1h10v6H5L2 9V7H1z" fill="none" stroke="#fff"/></svg>0</span></div>
  </div>
  <h3>Porro quisquam est qui</h3>
  <p>It has survived not only five centuries, but also the leap into electronic typesetting,</p>
  <a href="#">Read More »</a>
</article>
<article class="abs post post-3">
  <div class="post-image" role="img" aria-label="Photo of a ring being placed on a hand">
    <div class="post-meta"><span class="post-date">Dec 03</span><span class="post-comments"><svg width="12" height="10" viewBox="0 0 12 10"><path d="M1 1h10v6H5L2 9V7H1z" fill="none" stroke="#fff"/></svg>0</span></div>
  </div>
  <h3>Dolorem ipsum quia dolor</h3>
  <p>It has survived not only five centuries, but also the leap into electronic typesetting,</p>
  <a href="#">Read More »</a>
</article>

<footer class="abs site-footer"></footer>
<div class="abs footer-brand"><span class="brand-mark"></span><span class="brand-name">Vows and Farewells by Meg</span></div>
<div class="abs footer-heading" style="left:366px">CONTACT US</div>
<ul class="abs contact-list">
  <li><svg width="10" height="14" viewBox="0 0 10 14"><path d="M5 0a5 5 0 0 0-5 5c0 4 5 9 5 9s5-5 5-9a5 5 0 0 0-5-5zm0 7a2 2 0 1 1 0-4 2 2 0 0 1 0 4z" fill="#fff"/></svg><span>48 Orchard Lane,London,<br>N4 2QX, UK</span></li>
  <li><svg width="12" height="12" viewBox="0 0 24 24"><path fill="#fff" d="M6.6 10.8c1.4 2.8 3.8 5.1 6.6 6.6l2.2-2.2c.3-.3.7-.4 1-.2 1.1.4 2.3.6 3.6.6.6 0 1 .4 1 1V20c0 .6-.4 1-1 1C10.6 21 3 13.4 3 4c0-.6.4-1 1-1h3.5c.6 0 1 .4 1 1 0 1.3.2 2.5.6 3.6.1.3 0 .7-.2 1z"/></svg><span>+1 555-010-4421</span></li>
  <li><svg width="12" height="10" viewBox="0 0 12 10"><path d="M0 0h12v10H0z" fill="#fff"/><path d="M0 0l6 5 6-5" fill="none" stroke="#0d0d0d"/></svg><span>info@vowsandfarewells.example</span></li>
</ul>
<div class="abs footer-heading" style="left:647px">SIGN UP FOR NEWSLETTER</div>
<p class="abs newsletter-note">Your about us information would fit here nicely.</p>
<div class="abs newsletter-form"><span class="field">Email address</span><span class="submit">Submit</span></div>
<div class="abs footer-heading" style="left:942px">FOLLOW US OUT THERE</div>
<div class="abs social" aria-label="Social media links"><span></span><span></span><span></span><span></span></div>
<div class="abs footer-bar">Copyright © 2018. All Rights Reserved</div>

</body>
</html>
```